Editorial / Brochure Designer – Adobe InDesign Luxury Travel Publication Redesign

CREATIVE BRIEF
Editorial / Brochure Designer – Adobe InDesign
Luxury Travel Publication Redesign

Project:
Company brochure redesign — Wandering Horizons for Harbor Lanterns. Premium, full-color print publication.

Current State:
106-page brochure built on a stock design template. While the content foundation is strong, the design and layout repeat the same formula across all seven major sections.

Target Length:
Approximately 75–85 pages after planned content edits and consolidation. We are open to the designer's recommendations once the revised copy is reviewed and flowed into the new design.

Format:
8.5" × 11" portrait finished pages with 11" × 17" facing-page spreads. Full-color professional print production. Final binding is TBD, likely perfect/PUR perfect binding.

Audience:
Existing referral clients, including clients we would like to re-engage, as well as new referrals. Our clients are loyal, often multigenerational, higher-end travelers planning meaningful vacations, celebrations, and bucket-list journeys.

Primary Goal:
Create an evergreen "keep and refer back to" publication—not a seasonal mailer. The brochure should avoid dates, "new in 2027" messaging, or other content that will quickly expire.

Brand Feel:
Personal, relationship-driven, sophisticated, inspiring and "different and outside the box." It should not feel like a generic luxury travel agency brochure or stock/template design.

Think premium travel magazine / coffee-table publication rather than a traditional travel catalog.

Must Avoid:
Template monotony. The existing brochure relies heavily on the same layout skeleton:

Section divider → headline → pitch → bullet list → repeat

The redesigned publication must introduce variety in pacing, layout, photography, typography, white space, and visual rhythm from section to section, while still feeling cohesive and unmistakably Harbor Lanterns.

The Design Challenge
This is not simply a cleanup or reformatting project.

The selected designer will receive the existing 106-page brochure as the content foundation, along with revised/trimmed copy, brand assets, photography, and detailed editorial recommendations.

We want you to approach the publication with fresh eyes and a new creative perspective.

Some pages may need to become dramatic two-page spreads. Others may need to be minimal and quiet. Some information may work better as an editorial feature, comparison, sidebar, testimonial, pull quote, or visual story.

We want a designer who understands editorial pacing across a long publication, rather than simply creating an attractive template and repeating it.

Planned Content Changes/Priorities
The revised publication will include changes such as:

• Eliminating repetitive pages and messaging
• Creating one strong "Why Harbor Lanterns" narrative
• Adding a personal "Meet Rosa" / founder story
• A personal "Meet Rosa" spread near the front — photo, founder story, why referrals are the only marketing you've ever needed
• A short "how we've grown" page/timeline showing the range of travel you now cover
• Introducing recurring "Rosa's Pick" editorial callouts
• Incorporating authentic client stories/testimonials per major section
• Removing or relocating time-sensitive content
• Section openers that feel distinct from each other in layout, not just in photo subject
• Strengthening the final call to action
• Bringing more personality and Harbor Lanterns-specific storytelling into the publication

We specifically want someone with demonstrated experience designing:

• 50–150+ page publications
• Magazines
• Luxury brochures
• Product catalogs
• Lookbooks
• High-end print collateral
• Professional print publications

Experience with luxury travel, hospitality, lifestyle, cruise, resort, or premium consumer brands is highly desirable.

Advanced Adobe InDesign expertise is required, including Parent/Master Pages, paragraph and character styles, grids, long-document workflows, typography, image management, preflight, CMYK, bleeds, packaging, and professional print-ready PDF production.

We want to evaluate your:
• Creative direction
• Editorial judgment
• Typography
• Photography treatment
• Visual hierarchy
• Use of white space
• Page-to-page pacing
• Ability to elevate our existing brand

The successful designer will then be considered for the complete 75–85+ page publication redesign.

To Apply
Please provide:

• 2–4 examples of long-form publications you personally designed, preferably 50+ pages.
• Your experience with professional print production.
• Confirmation that you work in Adobe InDesign and can provide packaged source files so that we can edit at a later date.

Please prioritize relevant editorial work. We are specifically looking for long-form publication design experience, rather than portfolios focused primarily on logos, social media, websites, Canva templates, single-page flyers, or short brochures.

```html
<!DOCTYPE html>
<html lang="en">
<head>
<meta charset="utf-8">
<title>Wandering Horizons — Harbor Lanterns Brochure Pages</title>
<link rel="stylesheet" href="https://fonts.googleapis.com/css2?family=Playfair+Display:ital,wght@0,400;0,700;1,400;1,700;1,900&family=Inter:wght@400;700&display=swap">
<style>
  :root {
    --backdrop: #e3e3e3;
    --paper: #ffffff;
    --paper-soft: #f4f5f6;
    --heading-blue: #1f6793;
    --card-teal: #176f8c;
    --accent-red: #b4202d;
    --ink: #3a3a3a;
    --ink-soft: #5d5d5d;
    --sea: #3fb6d4;
    --sky: #9fd3ea;
    --sand: #eadbc4;
    --fjord-deep: #1d4f7a;
    --fjord-green: #5f9a3a;
    --card-line: #2b7396;
  }
  * { box-sizing: border-box; margin: 0; padding: 0; }
  html, body { width: 933px; height: 1200px; overflow: hidden; }
  body {
    background: var(--backdrop);
    font-family: "Inter", Arial, sans-serif;
    color: var(--ink);
    position: relative;
  }
  .page {
    position: absolute;
    overflow: hidden;
    background: var(--paper);
    box-shadow: 0 2px 8px rgba(0,0,0,0.12);
  }
  .photo { position: absolute; }
  .footer {
    position: absolute;
    bottom: 8px;
    font-size: 5px;
    color: var(--ink-soft);
    letter-spacing: 0.02em;
  }

  /* ---------- Row 1: contents spread + cover ---------- */
  .contents-left { left: 34px; top: 60px; width: 280px; height: 362px; }
  .contents-right { left: 314px; top: 60px; width: 280px; height: 362px; }
  .cover { left: 618px; top: 60px; width: 280px; height: 362px; }

  .beach-photo {
    inset: 0;
    background: linear-gradient(180deg, #cfe7f5 0%, #8fcbe6 38%, #49b9d3 62%, #7fd0dc 72%, var(--sand) 84%, #e9dccb 100%);
  }
  .contents-title {
    position: absolute;
    right: 18px;
    top: 40px;
    font-family: "Playfair Display", Georgia, serif;
    font-style: italic;
    font-weight: 700;
    font-size: 25px;
    line-height: 0.95;
    color: var(--heading-blue);
    text-align: right;
  }
  .contents-title .arrow { color: var(--accent-red); font-style: normal; font-size: 14px; }

  .contents-right .lagoon-photo {
    left: 0; right: 0; bottom: 0; height: 170px;
    background: linear-gradient(180deg, #d8eef6 0%, #7bcbe2 40%, #2aa9c9 100%);
  }
  .contents-panel {
    position: absolute;
    left: 16px; right: 16px; top: 24px;
    height: 190px;
    background: var(--paper);
    border-radius: 10px;
    padding: 14px 14px;
  }
  .contents-list { list-style: none; }
  .contents-list li { margin-bottom: 6px; }
  .contents-list .entry {
    display: block;
    font-style: italic;
    font-size: 7.5px;
    color: var(--card-teal);
  }
  .contents-list .note {
    display: block;
    font-style: italic;
    font-size: 5.5px;
    color: var(--ink-soft);
  }
  .legacy-line {
    position: absolute;
    left: 18px; bottom: 40px;
    font-family: "Playfair Display", Georgia, serif;
    color: #fff;
  }
  .legacy-line .kicker { display: block; font-style: italic; font-size: 8px; }
  .legacy-line .title { display: block; font-style: italic; font-weight: 700; font-size: 20px; line-height: 1.05; }

  .fjord-photo {
    inset: 0;
    background: linear-gradient(160deg, #6d8fb7 0%, #3e6fa3 28%, var(--fjord-deep) 58%, #2a6f84 80%, var(--fjord-green) 100%);
  }
  .cover-title {
    position: absolute;
    left: 40px; top: 78px;
    font-family: "Playfair Display", Georgia, serif;
    color: #fff;
    line-height: 0.9;
  }
  .cover-title .first { display: block; font-size: 30px; }
  .cover-title .second { display: block; font-size: 40px; padding-left: 10px; }
  .cover-tagline {
    position: absolute;
    left: 44px; top: 170px;
    font-family: "Playfair Display", Georgia, serif;
    font-size: 11px;
    line-height: 1.25;
    color: #fff;
  }
  .cover-brand {
    position: absolute;
    left: 0; right: 0; bottom: 40px;
    text-align: center;
    font-family: "Playfair Display", Georgia, serif;
    font-size: 15px;
    letter-spacing: 0.14em;
    color: #fff;
  }

  /* ---------- Row 2: story spread ---------- */
  .story-left { left: 26px; top: 452px; width: 440px; height: 570px; }
  .story-right { left: 466px; top: 452px; width: 440px; height: 570px; }

  .story-backdrop {
    inset: 0;
    background: linear-gradient(180deg, #b6d9e8 0%, #7fb06e 45%, #6aa5c0 70%, var(--sand) 100%);
  }
  .story-panel {
    position: absolute;
    left: 30px; right: 0; top: 22px; bottom: 22px;
    background: var(--paper);
  }
  .brand-mark {
    position: absolute;
    right: 20px; top: 16px;
    font-family: "Playfair Display", Georgia, serif;
    font-size: 12px;
    letter-spacing: 0.06em;
    color: var(--heading-blue);
    display: flex; align-items: center; gap: 5px;
  }
  .brand-mark .dot {
    width: 8px; height: 8px; border-radius: 50%;
    background: var(--heading-blue);
  }
  .friends-photo {
    left: 190px; right: 0; top: 120px; height: 330px;
    background: linear-gradient(180deg, #e8dccd 0%, #a9c5cf 35%, #6f99a8 60%, #3f6f8f 100%);
  }
  .story-copy {
    position: absolute;
    left: 22px; top: 92px;
    width: 205px;
    background: var(--paper);
    padding: 0 14px 14px 0;
  }
  .story-kicker {
    font-family: "Playfair Display", Georgia, serif;
    font-size: 15px;
    line-height: 1.1;
    color: var(--heading-blue);
  }
  .story-rule { width: 34px; height: 1px; background: var(--heading-blue); margin: 12px 0 10px; }
  .story-headline {
    font-family: "Playfair Display", Georgia, serif;
    font-style: italic;
    font-weight: 900;
    font-size: 27px;
    line-height: 1.02;
    color: var(--accent-red);
    margin-bottom: 12px;
  }
  .story-copy p {
    font-size: 6.6px;
    line-height: 1.45;
    color: var(--ink);
    margin-bottom: 6px;
  }
  .story-closer {
    position: absolute;
    left: 28px; bottom: 40px;
    font-family: "Playfair Display", Georgia, serif;
    font-size: 14px;
    color: var(--heading-blue);
  }

  .why-heading {
    position: absolute;
    left: 0; right: 0; top: 32px;
    text-align: center;
    font-family: "Playfair Display", Georgia, serif;
  }
  .why-heading .lead { display: block; font-size: 16px; color: var(--heading-blue); }
  .why-heading .name {
    display: block;
    font-style: italic; font-weight: 700;
    font-size: 29px;
    letter-spacing: 0.01em;
    color: var(--accent-red);
    line-height: 1.05;
  }
  .reason-grid {
    position: absolute;
    left: 28px; top: 108px;
    width: 384px;
    display: grid;
    grid-template-columns: 1fr 1fr;
    gap: 8px 10px;
  }
  .reason-card {
    border: 1px solid var(--card-line);
    height: 84px;
    padding: 12px 10px 8px 10px;
  }
  .reason-head { display: flex; align-items: center; gap: 8px; margin-bottom: 8px; }
  .reason-head svg { width: 24px; height: 24px; flex: none; }
  .reason-title {
    font-weight: 700;
    font-size: 7.4px;
    line-height: 1.25;
    letter-spacing: 0.02em;
    text-transform: uppercase;
    color: var(--card-teal);
  }
  .reason-text { font-size: 6.8px; line-height: 1.4; color: var(--ink); padding-left: 10px; }

  .specialists-photo {
    left: 0; right: 0; bottom: 0; height: 190px;
    background: linear-gradient(180deg, rgba(255,255,255,1) 0%, #d9eef2 30%, #7fd0d8 60%, #3aa9c4 85%, #2e6f9e 100%);
  }
  .specialists-title {
    position: absolute;
    left: 28px; top: 406px;
    font-family: "Playfair Display", Georgia, serif;
    font-size: 15px;
    line-height: 1.1;
    color: var(--heading-blue);
  }
  .specialists-list {
    position: absolute;
    left: 262px; top: 402px;
    list-style: none;
    font-size: 6.4px;
    line-height: 1.45;
    color: var(--ink);
  }
  .specialists-list li::before { content: "•"; color: var(--accent-red); margin-right: 3px; }
</style>
</head>
<body>

  <!-- Contents spread, left page -->
  <section class="page contents-left">
    <div class="photo beach-photo" role="img" aria-label="Tropical beach with a leaning palm tree over turquoise water"></div>
    <h2 class="contents-title">Table of<br>Contents <span class="arrow">⟶</span></h2>
    <span class="footer" style="left:14px;">toll-free 1-800-555-0142</span>
  </section>

  <!-- Contents spread, right page -->
  <section class="page contents-right">
    <div class="photo lagoon-photo" role="img" aria-label="Family wading in a clear turquoise lagoon"></div>
    <div class="contents-panel">
      <ul class="contents-list">
        <li><span class="entry">Why Harbor Lanterns</span><span class="note">How we help you plan the trip that matters</span></li>
        <li><span class="entry">Legacy Travel</span><span class="note">Multigenerational family journeys</span></li>
        <li><span class="entry">River Cruising</span><span class="note">Every river tells a story</span></li>
        <li><span class="entry">Alaska Travel</span><span class="note">Glaciers, wildlife, and wild coastline</span></li>
        <li><span class="entry">Expedition Travel</span><span class="note">Antarctica, the Galápagos, and beyond</span></li>
        <li><span class="entry">Ocean Cruise Voyages</span><span class="note">Iconic ships, endless amenities</span></li>
        <li><span class="entry">All-Inclusive Travel</span><span class="note">Everything taken care of</span></li>
        <li><span class="entry">Incentive Travel</span><span class="note">Extraordinary results deserve extraordinary experiences</span></li>
        <li><span class="entry">Ready to Start Planning?</span><span class="note">Next steps and contact information</span></li>
      </ul>
    </div>
    <div class="legacy-line">
      <span class="kicker">The Time You Share Today</span>
      <span class="title">Family's Legacy<br>Tomorrow</span>
    </div>
    <span class="footer" style="right:14px; color:#fff;">harborlanterns.example</span>
  </section>

  <!-- Cover -->
  <section class="page cover">
    <div class="photo fjord-photo" role="img" aria-label="Aerial view of a cruise ship sailing through a green fjord"></div>
    <h1 class="cover-title"><span class="first">Wandering</span><span class="second">Horizons</span></h1>
    <p class="cover-tagline">One<br>Trusted<br>Concierge</p>
    <div class="cover-brand">HARBOR LANTERNS</div>
  </section>

  <!-- Story spread, page 4 -->
  <section class="page story-left">
    <div class="photo story-backdrop" role="img" aria-label="Palm-lined tropical shoreline"></div>
    <div class="story-panel">
      <div class="brand-mark"><span class="dot"></span>HARBOR LANTERNS</div>
      <div class="photo friends-photo" role="img" aria-label="Two friends taking a selfie on seaside rocks"></div>
      <div class="story-copy">
        <p class="story-kicker">We Don't Just<br>Plan Vacations.</p>
        <div class="story-rule"></div>
        <h2 class="story-headline">We Create<br>Memories<br>That Last</h2>
        <p>For nearly 30 years, Harbor Lanterns has helped travelers explore the world with confidence, personalized service, and unforgettable experiences.</p>
        <p>Whether you're celebrating a milestone, bringing generations together, rewarding your team, or finally taking the bucket-list vacation you've always imagined, our mission remains the same.</p>
        <p>To make every journey effortless, meaningful, and unforgettable.</p>
        <p>From your first conversation until you return home, our team is by your side—offering expert guidance, managing every detail, and providing peace of mind before, during, and after your travels.</p>
        <p>Because extraordinary vacations don't happen by chance.</p>
      </div>
      <p class="story-closer">They happen through experience.</p>
      <span class="footer" style="right:18px;">harborlanterns.example | 4</span>
      <span class="footer" style="left:28px; bottom:4px;">toll-free 1-800-555-0142</span>
    </div>
  </section>

  <!-- Story spread, page 5 -->
  <section class="page story-right">
    <div class="photo specialists-photo" role="img" aria-label="Aerial view of a white-sand beach and turquoise sea with boats"></div>
    <h2 class="why-heading"><span class="lead">Why Travelers Choose</span><span class="name">HARBOR LANTERNS</span></h2>

    <div class="reason-grid">
      <article class="reason-card">
        <div class="reason-head">
          <svg viewBox="0 0 24 24" fill="none" stroke="#b4202d" stroke-width="1.8" aria-hidden="true"><path d="M7 4h10v5a5 5 0 0 1-10 0z" fill="#b4202d"/><path d="M7 6H4a3 3 0 0 0 3 4M17 6h3a3 3 0 0 1-3 4M12 14v4M8 20h8"/></svg>
          <h3 class="reason-title">Nearly 30 years of<br>expertise</h3>
        </div>
        <p class="reason-text">Trusted travel advisors creating unforgettable journeys since 1997.</p>
      </article>
      <article class="reason-card">
        <div class="reason-head">
          <svg viewBox="0 0 24 24" fill="none" stroke="#b4202d" stroke-width="1.8" aria-hidden="true"><circle cx="12" cy="12" r="10"/><path d="M15.5 8.5 13 13l-4.5 2.5L11 11z" fill="#b4202d"/></svg>
          <h3 class="reason-title">Personalized<br>vacation design</h3>
        </div>
        <p class="reason-text">Every itinerary is thoughtfully tailored to your travel style, interests, budget, and goals.</p>
      </article>
      <article class="reason-card">
        <div class="reason-head">
          <svg viewBox="0 0 24 24" fill="#b4202d" aria-hidden="true"><path d="M3 17a9 9 0 0 1 18 0z"/><rect x="2" y="18" width="20" height="2"/><circle cx="12" cy="7" r="1.5"/></svg>
          <h3 class="reason-title">Concierge-level<br>service</h3>
        </div>
        <p class="reason-text">From planning and documentation to dining reservations and special requests—we manage every detail.</p>
      </article>
      <article class="reason-card">
        <div class="reason-head">
          <svg viewBox="0 0 24 24" fill="none" stroke="#b4202d" stroke-width="1.8" stroke-linejoin="round" aria-hidden="true"><path d="M2 9l4-3 4 2 3-1 4 1 5 1-4 7-5 3-5-3z"/><path d="M9 12l2 2M11 11l3 3M13 10l3 3"/></svg>
          <h3 class="reason-title">Global preferred<br>partnerships</h3>
        </div>
        <p class="reason-text">with the world's leading cruise lines, resorts, tour operators, and luxury travel brands.</p>
      </article>
      <article class="reason-card">
        <div class="reason-head">
          <svg viewBox="0 0 24 24" fill="none" stroke="#b4202d" stroke-width="2" aria-hidden="true"><path d="M4 14v-2a8 8 0 0 1 16 0v2"/><rect x="3" y="13" width="4" height="6" rx="1" fill="#b4202d"/><rect x="17" y="13" width="4" height="6" rx="1" fill="#b4202d"/><path d="M19 19c0 2-2 3-5 3"/></svg>
          <h3 class="reason-title">Here when you<br>need us</h3>
        </div>
        <p class="reason-text">Personal support before, during, and after your journey.</p>
      </article>
      <article class="reason-card">
        <div class="reason-head">
          <svg viewBox="0 0 24 24" fill="none" stroke="#b4202d" stroke-width="2" aria-hidden="true"><path d="M12 21 3.5 12.5A5 5 0 0 1 12 6a5 5 0 0 1 8.5 6.5z"/></svg>
          <h3 class="reason-title">Passionate<br>about travel</h3>
        </div>
        <p class="reason-text">We love what we do and it shows in every vacation we plan and every relationship we build.</p>
      </article>
    </div>

    <h3 class="specialists-title">Specialists in<br>Extraordinary Travel</h3>
    <ul class="specialists-list">
      <li>Luxury Ocean and River Cruises</li>
      <li>Alaska and Expedition Travel</li>
      <li>Luxury Resorts</li>
      <li>Multigenerational Vacations</li>
      <li>Groups and Incentive Travel</li>
      <li>Private and Hosted Journeys</li>
    </ul>
    <span class="footer" style="left:20px;">5&nbsp;&nbsp;|&nbsp;&nbsp;toll-free 1-800-555-0142</span>
    <span class="footer" style="right:20px; color:#fff;">harborlanterns.example</span>
  </section>

</body>
</html>
```